Corportate Power Point Template

We need a corporate PPT Design for our startup Big Data company.

Basically, our company will ingest, analyze and generate dynamic Dashboards with data consumed from different sources like Social Networks, Enterprise Legacy Systems such as e-Commerce, ERP, CRM and others.

Company is headquartered in Brazil, but will have a global presence.

Industry/Entity Type

It Company

```html
<!DOCTYPE html>
<html lang="en">
<head>
<meta charset="utf-8">
<title>Title Presentation</title>
<link rel="stylesheet" href="https://fonts.googleapis.com/css2?family=Source+Sans+3:wght@500;600;700&display=swap">
<style>
  :root {
    --bg: #ffffff;
    --ink-grey: #545659;
    --brand-orange: #f07a2a;
    --tile-dark: #2f2f31;
    --tile-mid: #7a7a7c;
    --tile-orange: #f26522;
    --tile-light-orange: #f9a04a;
  }
  html, body {
    margin: 0;
    padding: 0;
    overflow: hidden;
    background: var(--bg);
  }
  .slide {
    position: relative;
    width: 1200px;
    height: 675px;
    overflow: hidden;
    background: var(--bg);
    font-family: "Source Sans 3", "Segoe UI", Arial, sans-serif;
  }
  .tile-motif {
    position: absolute;
    left: 15px;
    top: 75px;
    width: 250px;
    height: 520px;
    border-radius: 4px;
    background: linear-gradient(180deg,
      var(--tile-dark) 0%,
      var(--tile-mid) 38%,
      var(--tile-orange) 55%,
      var(--tile-light-orange) 78%,
      rgba(249, 160, 74, 0.35) 100%);
    opacity: 0.9;
  }
  .title-block {
    position: absolute;
    right: 60px;
    top: 236px;
    text-align: right;
  }
  .brand-name {
    display: inline-flex;
    align-items: center;
    gap: 10px;
    margin: 0 0 6px;
    font-size: 36px;
    font-weight: 600;
    line-height: 1;
    color: var(--brand-orange);
    letter-spacing: -0.3px;
  }
  .brand-mark {
    width: 24px;
    height: 24px;
    background: var(--ink-grey);
  }
  .slide-title {
    margin: 0;
    font-size: 66px;
    font-weight: 700;
    line-height: 1.1;
    color: var(--ink-grey);
    letter-spacing: -0.5px;
  }
  .slide-subtitle {
    margin: 4px 0 0;
    font-size: 38px;
    font-weight: 700;
    line-height: 1.1;
    color: var(--brand-orange);
  }
</style>
</head>
<body>
  <main class="slide">
    <div class="tile-motif" role="img" aria-label="Decorative column of grey and orange square tiles in perspective"></div>

    <header class="title-block">
      <p class="brand-name"><span class="brand-mark"></span>SummitGrid</p>
      <h1 class="slide-title">TITLE PRESENTATION</h1>
      <p class="slide-subtitle">Sub Title Presentation</p>
    </header>
  </main>
</body>
</html>
```